Travel video blogger needs website design

I need a website designed for my new travel video blog "Roaming Sparrow". I have only just started but need a website that is fairly simple and not too busy. I have a logo which I want on it (I have attached it to this project). I also want a link to all my other social medias on the main page (vidtrekhub, Snapwell and Palnook) and my videos as well. Here is a link to my vidtrekhub page for you to look at: https://www.vidtrekhub.net/channel/QRm4tZ8pWnE2HX57YKccd31v
As I have only just started and I am still trying to find my specific niche, again I need it to be sleek and simple that I can go in and change slightly here and there. I would like these pages on the website: About Me, Videos, Social Media, Blog, Gallery, contact me. for an example I like the look of www.theroamingkinfolk.net website.

I already have the domain and I am with Harborweb with pagecraftr.org. I just want to spend my time getting better and learning about videos then trying to create a website (I am a bit of a perfectionist when I try to do something).

Target Market(s)

Young Adults (majority females) between the ages of 18 and 30 with an interest in travelling.

Industry/Entity Type

Travel Industry

Number of Pages Required

1 page

Colors

Designer to choose colors to be used in the design.

Requirements
Must have
• A like to my Snapwell, Palnook and vidtrekhub channels on the home page
• Must be a nice, simple design
• Must have my logo on the front and name "Roaming Sparrow"
Nice to have
• A nice light, bright coloured theme
Should not have
• A dark coloured theme

```html
<!DOCTYPE html>
<html lang="en">
<head>
<meta charset="utf-8">
<title>Roaming Sparrow – Guatemala</title>
<link href="https://fonts.googleapis.com/css2?family=Caveat+Brush&family=Montserrat:wght@400&family=Open+Sans:wght@400;700&display=swap" rel="stylesheet">
<style>
  :root{
    --page:#ffffff;
    --ink:#222222;
    --body-text:#3a3a3a;
    --link:#2d6fe0;
    --brand-tan:#e2b583;
    --footer:#1f1d1e;
    --footer-base:#161415;
    --footer-link:#a7a4a5;
    --footer-head:#ffffff;
    --accent:#1aa3c8;
  }
  *{box-sizing:border-box;margin:0;padding:0}
  html,body{width:714px;height:1200px;overflow:hidden;background:var(--page)}
  body{position:relative;font-family:"Open Sans",Arial,sans-serif;color:var(--ink)}

  .brand{position:absolute;top:15px;left:0;width:714px;display:flex;justify-content:center;align-items:center;gap:8px}
  .brand-dot{width:42px;height:42px;border-radius:50%;background:var(--brand-tan)}
  .brand-name{font-family:"Montserrat",Arial,sans-serif;font-size:12px;letter-spacing:1px;color:var(--ink)}

  .main-nav{position:absolute;top:72px;left:0;width:714px;display:flex;justify-content:center;gap:21px;font-family:"Montserrat",Arial,sans-serif;font-size:8.8px;letter-spacing:.4px}
  .main-nav a{color:var(--ink);text-decoration:none}

  .video-hero{position:absolute;left:98px;top:107px;width:506px;height:202px;background:linear-gradient(135deg,#c98a3e 0%,#3fb3b0 40%,#1e9aa3 60%,#d9a45c 85%,#5a9b3a 100%)}
  .video-title{position:absolute;left:0;top:36px;width:100%;text-align:center;font-family:"Caveat Brush",cursive;font-size:38px;color:#fff}
  .play-btn{position:absolute;left:233px;top:91px}

  .post-text{position:absolute;left:103px;top:331px;width:472px;font-size:8px;line-height:13.1px;color:var(--body-text)}
  .back-link{position:absolute;left:110px;top:438px;font-size:7.2px;color:var(--link);text-decoration:none}

  .destinations{position:absolute;left:78px;top:486px;width:547px;display:grid;grid-template-columns:repeat(3,176px);grid-template-rows:repeat(3,150px);column-gap:9.5px;row-gap:10px}
  .destination{position:relative;display:flex;align-items:center;justify-content:center;font-family:"Caveat Brush",cursive;font-size:27px;color:#fff;text-decoration:none;text-shadow:0 1px 3px rgba(0,0,0,.25)}
  .costarica{background:linear-gradient(180deg,#2f86e0,#1b5aa8 50%,#3f6d3a)}
  .cuba{background:linear-gradient(180deg,#cfe3f2,#d8c8a8 45%,#c43a3a 70%,#7a7066)}
  .portugal{background:linear-gradient(180deg,#3b94e0,#7cc0ea 45%,#d9e2e6 70%,#6a8a4a)}
  .france{background:linear-gradient(180deg,#ee9a92,#b8a2c4 45%,#6a7a9a)}
  .belgium{background:linear-gradient(180deg,#9fb3d0,#d29a4e 50%,#6a4a2e)}
  .jamaica{background:linear-gradient(135deg,#3f6a3a,#7ea88a 50%,#2f5a2a)}
  .singapore{background:linear-gradient(180deg,#7c7fc4,#c2b5d8 50%,#8a86a8)}
  .greece{background:linear-gradient(135deg,#cfe0f2,#f4f4f6 40%,#2c5ab0 60%,#c8383a)}
  .australia{background:linear-gradient(180deg,#a9c8e4,#3fb0b8 40%,#e7d9c0 65%,#d6c4a0)}

  .site-footer{position:absolute;left:0;top:995px;width:714px;height:205px;background:var(--footer)}
  .footer-col{position:absolute;top:51px}
  .footer-col h3{font-size:11px;font-weight:700;color:var(--footer-head);letter-spacing:.3px;margin-bottom:8px;white-space:nowrap}
  .footer-col a{display:block;font-size:8.6px;line-height:13.6px;color:var(--footer-link);text-decoration:none;white-space:nowrap}
  .footer-col p{font-size:8.6px;line-height:12.8px;color:var(--footer-link);width:172px}
  .signup{display:flex;margin-top:16px;margin-left:3px}
  .signup input{width:115px;height:20px;border:0;padding-left:13px;font:400 8px "Open Sans",Arial,sans-serif;color:#333;background:#fff}
  .signup input::placeholder{color:#444}
  .signup button{width:33px;height:20px;border:0;background:var(--accent);color:#fff;font:400 11px "Open Sans",Arial,sans-serif}
  .footer-base{position:absolute;left:0;bottom:0;width:714px;height:25px;background:var(--footer-base);text-align:center;font-size:8.4px;line-height:25px;color:var(--footer-link)}
  .social-links{position:absolute;right:77px;top:0;display:flex;gap:12px}
  .social-links a{color:var(--footer-link);text-decoration:none;font-size:8.4px}
</style>
</head>
<body>

<header>
  <div class="brand">
    <span class="brand-dot"></span>
    <span class="brand-name">Roaming Sparrow</span>
  </div>
  <nav class="main-nav">
    <a href="#">ADVENTURES</a>
    <a href="#">ABOUT US</a>
    <a href="#">BLOG</a>
    <a href="#">SOCIAL MEDIA</a>
    <a href="#">SHOP</a>
    <a href="#">CONTACT US</a>
  </nav>
</header>

<main>
  <section class="video-hero" role="img" aria-label="Video preview: golden sea cliffs over a turquoise bay and sandy beach">
    <div class="video-title">Sneak Peek</div>
    <svg class="play-btn" width="40" height="40" viewBox="0 0 40 40" aria-hidden="true">
      <circle cx="20" cy="20" r="18" fill="rgba(0,0,0,.35)" stroke="#fff" stroke-width="2"/>
      <path d="M16 12 L29 20 L16 28 Z" fill="#fff"/>
    </svg>
  </section>

  <p class="post-text">Hola from Guatemala! We spent the week exploring Guatemala. There is so much adventure, culture and service here. The people here is what makes this place extra special. They treat you like family. A special thank you to Mayaventura for showing us all the wonder your country has to offer. During our time here, we teamed up with Clearspring Wells to learn more about the global water crisis. We went to multiple communities and villages to see their systems in action and how the people have benefited from clean drinking water. There is so much to be done and the great news is, we can fix this problem during our lifetime !We're joining the #PURE movement. You can donate to the PURE movement here.</p>

  <a class="back-link" href="#">Back to ADVENTURES</a>

  <section class="destinations">
    <a class="destination costarica" href="#" role="img" aria-label="Costa Rica: coastal bay with boats under a blue sky">costarica</a>
    <a class="destination cuba" href="#" role="img" aria-label="Cuba: classic cars parked along a colonial street">cuba</a>
    <a class="destination portugal" href="#" role="img" aria-label="Portugal: white seaside town above the ocean">portugal</a>
    <a class="destination france" href="#" role="img" aria-label="France: Paris skyline with the iron tower at dusk">france</a>
    <a class="destination belgium" href="#" role="img" aria-label="Belgium: guild houses and fountain on a market square">belgium</a>
    <a class="destination jamaica" href="#" role="img" aria-label="Jamaica: aerial view of boats in green water">jamaica</a>
    <a class="destination singapore" href="#" role="img" aria-label="Singapore: waterfront skyline at sunset">singapore</a>
    <a class="destination greece" href="#" role="img" aria-label="Greece: blue domed white houses of an island village">greece</a>
    <a class="destination australia" href="#" role="img" aria-label="Australia: kangaroo on a white sand beach">australia</a>
  </section>
</main>

<footer class="site-footer">
  <div class="footer-col" style="left:77px">
    <h3>ABOUT US</h3>
    <a href="#">About Theo</a><a href="#">Copyright</a><a href="#">Privacy Policy</a><a href="#">Contact</a>
  </div>
  <div class="footer-col" style="left:165px">
    <h3>COMMUNITY</h3>
    <a href="#">Travel Forum</a><a href="#">Book Club</a><a href="#">DRIFTA</a><a href="#">Guidebooks</a>
  </div>
  <div class="footer-col" style="left:260px">
    <h3>TRAVEL TIPS</h3>
    <a href="#">About Theo</a><a href="#">Copyright</a><a href="#">Privacy Policy</a><a href="#">Contact</a>
  </div>
  <div class="footer-col" style="left:349px">
    <h3>BOOK YOUR TRIP</h3>
    <a href="#">Travel Forum</a><a href="#">Book Club</a><a href="#">DRIFTA</a><a href="#">Guidebooks</a>
  </div>
  <div class="footer-col" style="left:466px">
    <h3>JOIN THE TRIBE</h3>
    <p>Join our Adventure Tribe to get the latest travel tips, stories, inspiration and a FREE adventure e-book.</p>
    <form class="signup">
      <input type="email" placeholder="Email">
      <button type="button">Go</button>
    </form>
  </div>
  <div class="footer-base">
    2018 all Rights reserved
    <nav class="social-links" aria-label="Social channels">
      <a href="https://www.vidtrekhub.net/channel/QRm4tZ8pWnE2HX57YKccd31v">vidtrekhub</a>
      <a href="https://www.snapwell.app/roamingsparrow">Snapwell</a>
      <a href="https://www.palnook.com/roamingsparrow">Palnook</a>
    </nav>
  </div>
</footer>

</body>
</html>
```